Travel Blogger Business Card for roamquill.net

I need a two-sided business card for a travel blogging website. The card should be both professional and fun at the same time. This is for the website www.roamquill.net

I don't necessarily think that the current logo on the website needs to be used on the business card but it can be. I am very flexible with ideas

Target Market(s)

Travel agencies that will be met at a conference.

Industry/Entity Type

Travel

Contact Information for Business Card

Company Name: Roam Quill.net
Name: Bertrand Olesky
Voice: +1-(345)-402-7731
Address: Coral Reach Shore, Grand Cayman, Cayman Islands
Email: ceo@roamquill.net

Colors
0592cd
0355a3
3176b5
33a6d7
85cae6
85acd3

Requirements
Must have
• Website address and name should be bigger than address, phone number, and email.

```html
<!DOCTYPE html>
<html lang="en">
<head>
<meta charset="utf-8">
<title>Roam Quill — Business Card</title>
<link rel="stylesheet" href="https://fonts.googleapis.com/css2?family=Orbitron:wght@700&family=Montserrat:wght@400;600&display=swap">
<style>
  :root {
    --backdrop: #2b2b2d;
    --teal: #0a8196;
    --teal-bright: #1a93a6;
    --ink: #0b0b0b;
    --paper: #ffffff;
    --text-dark: #222222;
  }
  * { margin: 0; padding: 0; box-sizing: border-box; }
  html, body { width: 1200px; height: 900px; overflow: hidden; }
  body {
    background: var(--backdrop);
    font-family: "Montserrat", sans-serif;
    position: relative;
  }
  .card {
    position: absolute;
    left: 250px;
    width: 700px;
    height: 400px;
    overflow: hidden;
    box-shadow: 0 14px 30px rgba(0,0,0,0.45);
  }
  .card-front { top: 30px; background: var(--teal); }
  .card-back { top: 470px; background: var(--ink); }

  .brand {
    font-family: "Orbitron", sans-serif;
    font-weight: 700;
    color: var(--paper);
    letter-spacing: 1px;
    white-space: nowrap;
    display: flex;
    align-items: center;
    gap: 14px;
  }
  .brand-dot {
    width: 14px; height: 14px;
    border-radius: 50%;
    background: var(--paper);
    flex: none;
  }
  .card-front .brand {
    position: absolute;
    left: 0; right: 0; top: 150px;
    justify-content: center;
    font-size: 46px;
  }
  .front-url {
    position: absolute;
    left: 0; right: 0; top: 300px;
    text-align: center;
    color: var(--paper);
    font-size: 18px;
    letter-spacing: 0.5px;
  }
  .front-url strong { font-weight: 600; }

  .wave { position: absolute; inset: 0; }
  .card-back .brand {
    position: absolute;
    left: 40px; top: 50px;
    font-size: 40px;
  }
  .contact {
    position: absolute;
    right: 38px; top: 116px;
    text-align: right;
    color: var(--paper);
    font-size: 15px;
  }
  .contact-name {
    color: var(--teal-bright);
    font-weight: 600;
    font-size: 17px;
    letter-spacing: 0.5px;
    margin-bottom: 8px;
    margin-right: 26px;
  }
  .contact-row {
    display: flex;
    justify-content: flex-end;
    align-items: center;
    gap: 10px;
    height: 22px;
  }
  .contact-row svg { width: 16px; height: 16px; flex: none; }
  .contact-url { font-size: 17px; }
  .contact-url strong { color: var(--teal-bright); font-weight: 600; }
  .address {
    position: absolute;
    left: 60px; bottom: 18px;
    color: var(--text-dark);
    font-size: 14px;
    line-height: 1.2;
  }
</style>
</head>
<body>

<section class="card card-front">
  <div class="brand"><span class="brand-dot"></span>ROAM QUILL</div>
  <p class="front-url">www.<strong>roamquill</strong>.net</p>
</section>

<section class="card card-back">
  <svg class="wave" viewBox="0 0 700 400" aria-hidden="true">
    <path d="M0 340 C60 340 110 190 165 192 C220 194 240 300 370 300 C490 300 600 260 700 225 L700 400 L0 400 Z" fill="var(--teal)"/>
    <path d="M0 352 C60 352 110 202 165 204 C220 206 240 312 370 312 C490 312 600 272 700 237 L700 400 L0 400 Z" fill="var(--paper)"/>
    <path d="M0 334 C60 334 110 184 165 186 C220 188 240 294 370 294 C490 294 600 254 700 219" fill="none" stroke="var(--paper)" stroke-width="1.5"/>
    <circle cx="607" cy="251" r="8" fill="var(--ink)"/>
    <circle cx="632" cy="243" r="6" fill="var(--ink)"/>
    <circle cx="654" cy="235" r="4" fill="var(--ink)"/>
  </svg>

  <div class="brand"><span class="brand-dot"></span>ROAM QUILL</div>

  <div class="contact">
    <p class="contact-name">BERTRAND OLESKY</p>
    <div class="contact-row"><span>+1-(345)-402-7731</span>
      <svg viewBox="0 0 16 16"><circle cx="8" cy="8" r="8" fill="var(--teal-bright)"/><path d="M5.2 4.2 l1.6 0 l0.6 2 l-1 0.8 q0.8 1.7 2.5 2.5 l0.8 -1 l2 0.6 l0 1.6 q-4.5 0.5 -6.5 -6.5z" fill="var(--ink)"/></svg>
    </div>
    <div class="contact-row"><span>ceo@roamquill.net</span>
      <svg viewBox="0 0 16 16"><circle cx="8" cy="8" r="8" fill="var(--teal-bright)"/><rect x="4" y="5" width="8" height="6" fill="none" stroke="var(--ink)" stroke-width="1.2"/><path d="M4 5 l4 3.5 l4 -3.5" fill="none" stroke="var(--ink)" stroke-width="1.2"/></svg>
    </div>
    <div class="contact-row"><span class="contact-url">www.<strong>roamquill</strong>.net</span>
      <svg viewBox="0 0 16 16"><circle cx="8" cy="8" r="8" fill="var(--teal-bright)"/><circle cx="8" cy="8" r="4.5" fill="none" stroke="var(--ink)" stroke-width="1.1"/><path d="M3.5 8 h9 M8 3.5 q-2.5 4.5 0 9 M8 3.5 q2.5 4.5 0 9" fill="none" stroke="var(--ink)" stroke-width="1"/></svg>
    </div>
  </div>

  <p class="address">Coral Reach Shore,<br>Grand Cayman,<br>Cayman Islands</p>
</section>

</body>
</html>
```